Stationary for Hair Cosmetic company

We mainly sell hair thickening products www.morvello-wellform.de/morvello-hair/ Hair thickening products are a smart and easy solution for thinning hair for both men and women. We sell very information oriented in an honest undramatic manner.

We would like to see a decent color and style that is suitable for men and women. It shall be rather modern with a vintage spin as our own product (Morvello Bottle). Please use our logo (attatched).

Please bias your design to the bottle. To give you an idea: Chalk design like http://de.pixaverum.com/id/48213597 or one-color watercolor like http://de.pixaverum.com/id/63925180 is appreciated but not necessary.

Good but rejected designs will get compensation.

Target Market(s)

Wide range in demographics: age 20-55; 45% male, 55% women; issues with hair loss; self-conscious

Industry/Entity Type

Hair

Colors
3377b5
33a6d7
32b7a4
cbdf83
fbf289
fee18a
f9bb93
f05157

Requirements
Must have
• trustworthiness
Nice to have
• Chalk design like http://de.pixaverum.com/id/48213597 or one-color watercolor like http://de.pixaverum.com/id/63925180 is appreciated but not necessary

```html
<!DOCTYPE html>
<html lang="en">
<head>
<meta charset="utf-8">
<title>Morvello Hair – Stationery</title>
<link href="https://fonts.googleapis.com/css2?family=Montserrat:wght@400;500&family=Arimo:wght@400;700&display=swap" rel="stylesheet">
<style>
  :root {
    --bg: #e4e4e2;
    --cover-blue: #2c62a6;
    --cover-pattern: #3a74b8;
    --spine-orange: #d8663c;
    --navy: #17324f;
    --navy-soft: #1f4467;
    --sky: #3aa6dc;
    --sky-light: #5cc0ea;
    --teal: #32b7a4;
    --red: #f05157;
    --paper: #ffffff;
    --ink: #333a40;
    --rule: #9aa3ab;
    --white: #ffffff;
  }
  * { box-sizing: border-box; margin: 0; padding: 0; }
  html, body { width: 1200px; height: 900px; overflow: hidden; }
  body {
    background: var(--bg);
    font-family: "Arimo", Arial, sans-serif;
    color: var(--ink);
    position: relative;
  }
  .brand-name {
    font-family: "Montserrat", Arial, sans-serif;
    font-weight: 400;
    letter-spacing: 0.28em;
    text-transform: uppercase;
    display: flex;
    align-items: center;
    gap: 8px;
  }
  .brand-dot {
    width: 8px; height: 8px; border-radius: 50%;
    background: currentColor; display: inline-block;
  }

  /* Notebook cover */
  .notebook {
    position: absolute; left: 300px; top: 50px;
    width: 340px; height: 470px;
    background: var(--cover-blue);
    display: flex;
  }
  .notebook-spine {
    width: 46px; height: 100%;
    background: linear-gradient(90deg,
      var(--spine-orange) 0 12px,
      var(--white) 12px 17px,
      var(--cover-blue) 17px 24px,
      var(--white) 24px 29px,
      var(--cover-blue) 29px 36px,
      var(--white) 36px 41px,
      var(--cover-blue) 41px 46px);
  }
  .notebook-face { position: relative; flex: 1; }
  .notebook-pattern {
    position: absolute; inset: 0;
    background: radial-gradient(circle at 50% 45%, var(--cover-pattern), var(--cover-blue) 75%);
  }
  .notebook-brand {
    position: absolute; right: 28px; bottom: 40px;
    color: var(--white); font-size: 22px;
    padding-bottom: 6px; border-bottom: 1px solid var(--white);
  }

  /* Cards */
  .card {
    position: absolute; top: 600px; width: 150px; height: 220px;
  }
  .card-label {
    left: 60px; background: var(--sky); color: var(--white);
    display: flex; flex-direction: column; align-items: center; text-align: center;
    padding-top: 22px;
  }
  .card-label .mark-area {
    width: 62px; height: 62px; border-radius: 50%;
    background: var(--sky-light);
  }
  .card-label .brand-name { font-size: 12px; margin-top: 10px; padding-bottom: 4px; border-bottom: 1px solid var(--white); }
  .card-label .product { font-size: 10px; margin-top: 12px; line-height: 1.6; }
  .card-label .volume { font-size: 10px; margin-top: 10px; letter-spacing: 0.1em; }

  .card-contact {
    left: 240px; background: var(--navy); color: var(--white);
    padding: 18px 14px;
  }
  .card-contact .pattern-area {
    position: absolute; right: 10px; top: 12px; width: 90px; height: 80px;
    background: radial-gradient(circle, var(--navy-soft), var(--navy) 70%);
  }
  .card-contact .name-tab {
    position: absolute; left: 14px; top: 110px;
    background: var(--sky); color: var(--white);
    font-size: 10px; padding: 4px 6px;
  }
  .card-contact .details {
    position: absolute; left: 14px; top: 140px;
    font-size: 7.5px; line-height: 1.55; color: #cfe3f2;
  }
  .card-contact .details strong { color: var(--white); font-weight: 700; }

  .card-front {
    left: 420px; background: var(--navy); overflow: hidden;
  }
  .card-front svg { position: absolute; inset: 0; }
  .card-front .brand-name {
    position: absolute; left: 50%; top: 50%;
    transform: translate(-50%, -50%) rotate(-90deg);
    color: var(--white); font-size: 15px; white-space: nowrap;
  }

  /* Letterhead */
  .letterhead {
    position: absolute; left: 700px; top: 40px;
    width: 440px; height: 622px;
    background: var(--paper);
    border-top: 1px dashed var(--rule);
    padding: 0;
  }
  .letterhead-rule-v {
    position: absolute; left: 48px; top: 0; bottom: 60px;
    border-left: 1px dashed var(--rule);
  }
  .letterhead-rule-h {
    position: absolute; left: 0; right: 0; top: 30px;
    border-top: 1px dashed var(--rule);
  }
  .letterhead-head {
    position: absolute; left: 70px; top: 22px;
    color: var(--sky); font-size: 20px;
    display: flex; flex-direction: column; align-items: center;
  }
  .letterhead-head svg { margin-bottom: 4px; }
  .letterhead-head .brand-name { padding: 0 4px 5px; border-bottom: 2px solid var(--sky); }
  .letterhead-seal {
    position: absolute; right: 24px; top: 80px;
    width: 52px; height: 52px; border-radius: 50%;
    background: #d9dcdf;
  }
  .letter-date { position: absolute; right: 90px; top: 120px; font-size: 9px; }
  .letter-body {
    position: absolute; left: 66px; right: 26px; top: 100px;
    font-size: 8.6px; line-height: 1.42;
  }
  .letter-body p { margin-bottom: 8px; }
  .letter-body .salutation { margin-bottom: 12px; }
  .letter-body .indent { text-indent: 14px; }
  .letterhead-footer {
    position: absolute; left: 66px; bottom: 80px;
    font-size: 8.6px; line-height: 1.4; color: var(--sky);
  }
  .letterhead-badges {
    position: absolute; right: 26px; bottom: 30px; display: flex; gap: 14px; align-items: center;
  }
  .badge { width: 34px; height: 34px; border-radius: 50%; }
  .badge-origin { background: #f2c431; border-radius: 4px; height: 24px; }
  .badge-eco { border: 2px solid #6a6f73; }
  .badge-cruelty { border: 3px solid var(--red); }
  .letterhead-band {
    position: absolute; left: 0; right: 0; bottom: 0; height: 10px; background: var(--red);
  }
</style>
</head>
<body>

  <section class="notebook" aria-label="Notebook cover">
    <div class="notebook-spine"></div>
    <div class="notebook-face">
      <div class="notebook-pattern" role="img" aria-label="Tone-on-tone blue repeating leaf pattern"></div>
      <div class="notebook-brand brand-name">Morvello</div>
    </div>
  </section>

  <section class="card card-label" aria-label="Product label card">
    <div class="mark-area" role="img" aria-label="Round emblem illustration in light blue"></div>
    <div class="brand-name">Morvello</div>
    <p class="product">Haarverdichter<br>Fülle &amp; Volumen<br>mit Biotin und Koffein</p>
    <p class="volume">100 ML</p>
  </section>

  <section class="card card-contact" aria-label="Business card back">
    <div class="pattern-area" role="img" aria-label="Faint navy leaf ornament"></div>
    <div class="name-tab brand-name">Morvello</div>
    <div class="details">
      <strong>Jana Korvell</strong><br>
      Geschäftsführung<br>
      Lindenhofstraße 14<br>
      61352 Bad Ostwald<br>
      Tel. 06172 480 219
    </div>
  </section>

  <section class="card card-front" aria-label="Business card front">
    <svg width="150" height="220" viewBox="0 0 150 220" aria-hidden="true">
      <polygon points="0,0 150,0 150,40 75,70 0,40" fill="var(--sky)"/>
      <polygon points="0,220 150,220 150,180 75,150 0,180" fill="var(--sky)"/>
      <rect x="55" y="20" width="40" height="180" fill="var(--sky-light)"/>
    </svg>
    <div class="brand-name">Morvello</div>
  </section>

  <section class="letterhead" aria-label="Letterhead">
    <div class="letterhead-rule-h"></div>
    <div class="letterhead-rule-v"></div>
    <header class="letterhead-head">
      <svg width="22" height="14" viewBox="0 0 22 14" aria-hidden="true"><polygon points="0,0 22,0 11,14" fill="var(--teal)"/></svg>
      <div class="brand-name">Morvello</div>
    </header>
    <div class="letterhead-seal" role="img" aria-label="Round leaf emblem in grey"></div>
    <p class="letter-date">31 January 2001</p>
    <div class="letter-body">
      <p class="salutation">Dear Tobias,</p>
      <p class="indent" style="margin-top:26px">On the Graphics List the other day, I got the strangest request, for a dummy letter. Surely a letter is easy enough to fake, and not something I would have thought needed special dummy text. Perhaps I am ignorant, but I kind of assumed it was a joke. Except that it wasn't very funny. Unless I'm just too ignorant to understand it. Is there some sort of official dummy text for letters? I certainly find that "lorem ipsum" stuff incredibly useful for large documents, so I assume it could be used for a letter as well, but the designer (corporate funster, whatever) of course would have to make up his or her own date and name and address.</p>
      <p class="indent">I usually take the time to write utter bollocks a la automatic writing for something as short as a letter. As long as it doesn't have the word "bollocks" in it, it amuses me and helps prepare myself for the task at hand.</p>
      <p class="indent">My Dear Mother and Sister, — I start to do Sandwich Islands day after tomorrow. (I suppose Greta is geographer enough by this time to find them on the map.) in the steamer "Ajax." We shall arrive there in about twelve days. My friends seem determined that I shall not lack acquaintances, for I only decided today to go, and they have already sent me letters of introduction to everybody down there worth knowing. I am to remain there a month and ransack the islands, the great cataracts and the volcanoes completely, and write twenty or thirty letters to the Sacramento Union — for which they pay me as much money as I would get if I staid at home.</p>
      <p class="indent">If I come back here I expect to start straight across the continent by way of the Columbia river, the Pend d'Oreille Lakes, through Montana and down the Missouri river — only 200 miles of land travel from San Francisco to New Orleans.</p>
      <p>Goodbye for the present.</p>
      <p>Yours,<br>Lene</p>
    </div>
    <footer class="letterhead-footer">
      Professional Product by Morvello Hair<br>
      Harlen und Dossberg GbR<br>
      Lindenhofstraße 14<br>
      61352 Bad Ostwald · www.Morvello-Hair.de
    </footer>
    <div class="letterhead-badges">
      <span class="badge badge-origin"></span>
      <span class="badge badge-eco"></span>
      <span class="badge badge-cruelty"></span>
    </div>
    <div class="letterhead-band"></div>
  </section>

</body>
</html>
```